Letterhead and Corporate Stationary Design Project

I would like the following designed:
1. Corporate Letterhead
2. Compliment Slips
3. Business Cards(2)

I have attached word document that outlines the text to be contained for all 3. The logo is fine as is and can be used in the design.
I only need letterhead to be designed for contest, the successful applicant can desisgn other 2 items after being awarded the job

Target Market(s)

Information Technology

Industry/Entity Type

Business

Requirements
Must have
• Border around entire letter that matches colours in logo
Clearly identifiable letterhead and footer
Nice to have
• Watermark

```html
<!DOCTYPE html>
<html lang="en">
<head>
<meta charset="utf-8">
<title>Corvane Business Solutions – Letterhead</title>
<link href="https://fonts.googleapis.com/css2?family=Arimo:wght@400&display=swap" rel="stylesheet">
<style>
  :root {
    --backdrop: #ececec;
    --frame-grey: #b7b9bb;
    --sheet: #f6f6f6;
    --navy: #2b4a8b;
    --sky: #2f8fc8;
    --ink: #4a4a4a;
    --rule: #a9a9a9;
  }
  html, body {
    margin: 0;
    padding: 0;
    width: 1200px;
    height: 795px;
    overflow: hidden;
    background: var(--backdrop);
  }
  .canvas {
    position: relative;
    width: 1200px;
    height: 795px;
  }
  .letterhead {
    position: absolute;
    left: 337px;
    top: 25px;
    width: 526px;
    height: 745px;
    box-sizing: border-box;
    padding: 13px;
    background: var(--frame-grey);
    box-shadow: 0 4px 14px rgba(0,0,0,0.12);
  }
  .sheet {
    position: relative;
    width: 100%;
    height: 100%;
    background: var(--sheet);
    border-radius: 10px;
    overflow: hidden;
  }
  .top-band {
    position: absolute;
    left: 0; right: 0; top: 0;
    height: 14px;
    background: var(--navy);
    border-radius: 10px 10px 0 0;
  }
  .brand {
    position: absolute;
    left: 30px;
    top: 62px;
    display: flex;
    align-items: center;
    gap: 8px;
    font-family: "Arimo", sans-serif;
    font-size: 18px;
    font-weight: 400;
    line-height: 1;
    color: var(--navy);
  }
  .brand-dot {
    width: 14px;
    height: 14px;
    border-radius: 50%;
    background: var(--sky);
    flex: none;
  }
  .sender {
    position: absolute;
    right: 26px;
    top: 28px;
    font-family: "Arimo", sans-serif;
    font-style: normal;
    font-size: 7.5px;
    line-height: 1.35;
    color: var(--ink);
    text-align: left;
  }
  .sender .web { color: var(--sky); }
  .header-rule {
    position: absolute;
    left: 30px;
    right: 26px;
    top: 100px;
    height: 0;
    border-top: 1px solid var(--rule);
  }
  .bottom-band {
    position: absolute;
    left: 0; right: 0; bottom: 0;
    height: 22px;
    background: var(--sky);
    border-radius: 0 0 10px 10px;
    display: flex;
    align-items: center;
    justify-content: center;
  }
  .legal {
    font-family: "Arimo", sans-serif;
    font-size: 7.5px;
    font-weight: 400;
    color: #ffffff;
    letter-spacing: 0.2px;
  }
</style>
</head>
<body>
<div class="canvas">
  <div class="letterhead">
    <div class="sheet">
      <div class="top-band"></div>

      <div class="brand">
        <span class="brand-dot"></span>
        <span class="brand-name">Corvane Business Solutions</span>
      </div>

      <address class="sender">
        Corvane Business Solutions<br>
        Unit 4, Harbour Court<br>
        12 Quay Street, Navan<br>
        Co. Meath, Ireland<br>
        <span class="web">www.corvane.ie</span><br>
        T: +353 46 901 2345
      </address>

      <div class="header-rule"></div>

      <div class="bottom-band">
        <span class="legal">Corvane Business Solutions Limited | Company Registration 517390 | VAT No IE5173904K</span>
      </div>
    </div>
  </div>
</div>
</body>
</html>
```